Web Design Project

We need a designer to help us with our ecommerce site, shopify. We will probably use a custom template in order to save costs. (http://www.brindlemoorbeanhouse.com/ is a good reference of what we want.)
Basically, our company is Mirova K and we are selling tshirts with social messages, and most of the profits will be going to these social enterprises. We are not selling tshirts, but instead, we are selling social messages to the masses.
We will like to use tshirts as vehicles to promote social messages among the youth, as such the designs and colour scheme should be colourful, in order to resonate with the youth. The website will be set up through Shopify.com, therefore our elected designer has to be familiar with the usage of the Shopify web design tools. The website should be as simple as possible; visually engaging while light on text, with subtle animation (eg. highlight product for alternate image) to engage our customers that visit the site.
Our logo will be Mirova K, with the tagline (tshirts for humanity).
In summary:
- Simple website showcasing T-shirt with social messages
- Done using Shopify.com
- Bright colour scheme
- Simple snazzy design based on references provided(I have attached the file for the site layout)
- Logo design
We are committed in driving social messages among the youth and we are looking for enthusiastic designers who can embody our concept and bring the design to life; elegantly integrating cool and social meanings together.
Lets work together and make this world a better place; We are not just tshirts with social meanings, we are humanity at its purest form.
Yours truly,
the team at Mirova K.
Target Market(s)
Youth. 18-24

```html
<!DOCTYPE html>
<html lang="en">
<head>
<meta charset="utf-8">
<title>Mirova K – T-shirts for humanity</title>
<link rel="stylesheet" href="https://fonts.googleapis.com/css2?family=Lobster&family=Open+Sans:wght@400;600&display=swap">
<style>
  :root {
    --green: #7cad1a;
    --green-dark: #6a9915;
    --grey-text: #8a8a8a;
    --ink: #222222;
    --line: #d9d9d9;
    --band: #f1f1f1;
    --white: #ffffff;
    --tab: #dcdcdc;
    --social-navy: #3b5998;
    --social-sky: #2ba9e1;
    --social-deep: #0e76a8;
    --social-orange: #f39422;
  }
  * { box-sizing: border-box; margin: 0; padding: 0; }
  html, body { width: 1000px; height: 1200px; overflow: hidden; background: var(--white); }
  body { position: relative; font-family: "Open Sans", Arial, sans-serif; color: var(--ink); }
  .abs { position: absolute; }
  .script { font-family: "Lobster", cursive; color: var(--green); font-weight: 400; }

  .header-bg { left: 0; top: 0; width: 1000px; height: 140px; background: linear-gradient(#ebebeb, #ffffff); }
  .brand { left: 41px; top: 44px; display: flex; align-items: center; gap: 12px; }
  .brand-mark { width: 26px; height: 26px; background: var(--green); }
  .brand-name { font-size: 36px; font-weight: 600; color: var(--green); line-height: 1; }

  .account-tab { left: 790px; top: 0; width: 181px; height: 42px; background: var(--tab); border-radius: 0 0 8px 8px;
    font-size: 14px; color: #555; display: flex; align-items: center; justify-content: center; gap: 9px; }
  .cart { left: 799px; top: 60px; display: flex; align-items: center; gap: 6px; }
  .cart-label { font-family: "Lobster", cursive; color: var(--green); font-size: 19px; }
  .cart-count { font-size: 13px; color: var(--green); }

  .main-nav { left: 483px; top: 92px; width: 517px; height: 38px; background: var(--green); border-radius: 6px 0 0 6px;
    display: flex; align-items: center; gap: 24px; padding-left: 43px; box-shadow: 0 8px 10px -6px rgba(0,0,0,.45); }
  .main-nav a { color: var(--white); text-decoration: none; font-size: 16.5px; }

  .hero-ornament { left: 505px; top: 145px; width: 495px; height: 435px;
    background: radial-gradient(ellipse at 80% 45%, #e4efcf 0%, #f1f6e6 45%, rgba(255,255,255,0) 72%); }
  .hero-shirt { left: 85px; top: 200px; width: 433px; height: 376px; border-radius: 30px 30px 6px 6px;
    background: radial-gradient(ellipse at 50% 45%, #7fb4a4 0%, #4f8a4c 45%, #3f7a3c 100%); }
  .hero-title { left: 555px; top: 300px; font-size: 34px; }
  .hero-text { left: 547px; top: 357px; width: 390px; font-size: 15.5px; line-height: 24px; color: var(--grey-text); letter-spacing: -0.2px; }
  .btn-quote { left: 547px; top: 473px; width: 174px; height: 36px; background: var(--green); color: var(--white);
    border-radius: 3px; font-size: 20px; display: flex; align-items: center; justify-content: center;
    box-shadow: 0 10px 10px -8px rgba(0,0,0,.35); }
  .slider-dots { left: 521px; top: 555px; }

  .divider { left: 30px; top: 607px; width: 940px; height: 2px; background: linear-gradient(90deg, rgba(0,0,0,0), #cfcfcf 50%, rgba(0,0,0,0)); }

  .section-title { font-size: 24px; }
  .featured-title { left: 66px; top: 626px; }
  .product-card { top: 672px; width: 201px; height: 154px; border: 1px solid var(--line); background: var(--white); }
  .product-art { position: absolute; left: 36px; top: 13px; width: 128px; height: 128px; border-radius: 18px 18px 4px 4px; }
  .art-black { background: linear-gradient(#1d1d1d, #111111); }
  .art-green { background: radial-gradient(ellipse at 50% 45%, #7fb4a4, #4a8547 60%); }
  .carousel-arrow { top: 729px; }

  .welcome-title { left: 71px; top: 849px; }
  .welcome-text { left: 73px; top: 894px; width: 573px; font-size: 12.4px; line-height: 19px; text-align: justify; color: var(--ink); letter-spacing: -0.15px; }

  .call-box { left: 670px; top: 872px; width: 263px; height: 136px; background: var(--green); box-shadow: 0 10px 10px -8px rgba(0,0,0,.3); }
  .call-photo { left: 820px; top: 872px; width: 113px; height: 136px; background: linear-gradient(90deg, #8fb83e, #f1e2d0 40%, #f6eee6); }
  .call-title { left: 681px; top: 910px; font-size: 23px; color: var(--white); }
  .call-phone { left: 678px; top: 947px; font-size: 15px; color: var(--white); }
  .btn-call { left: 691px; top: 984px; width: 128px; height: 31px; border-radius: 4px; background: linear-gradient(#ffffff, #cfcfcf);
    color: var(--green-dark); font-size: 16px; display: flex; align-items: center; justify-content: center; box-shadow: 0 2px 3px rgba(0,0,0,.3); }

  .partners-band { left: 0; top: 1039px; width: 1000px; height: 81px; background: var(--band); border-top: 1px solid #b8b8b8; }
  .partners-title { left: 58px; top: 1052px; font-size: 30px; }
  .partners-sub { left: 58px; top: 1087px; font-size: 14px; color: #333; }
  .partner-badge { top: 1055px; height: 46px; background: #cfcfcf; border-radius: 23px; }

  .footer { left: 0; top: 1120px; width: 1000px; height: 53px; background: var(--green); }
  .footer-nav { left: 47px; top: 1138px; display: flex; gap: 18px; }
  .footer-nav a { color: var(--white); text-decoration: none; font-size: 12px; }
  .follow { left: 700px; top: 1136px; font-size: 13px; color: var(--white); }
  .social { top: 1131px; width: 30px; height: 30px; border-radius: 50%; }
  .copyright { left: 45px; top: 1178px; font-size: 13px; color: #444; }
</style>
</head>
<body>
  <div class="abs header-bg"></div>

  <div class="abs brand">
    <span class="brand-mark"></span>
    <span class="brand-name">Mirova K</span>
  </div>

  <div class="abs account-tab"><span>Login</span><span>|</span><span>Shopping Cart</span></div>

  <div class="abs cart">
    <svg width="20" height="18" viewBox="0 0 20 18" aria-hidden="true">
      <path d="M1 6h18l-2.5 10h-13z" fill="none" stroke="var(--green)" stroke-width="2"/>
      <path d="M5 6l4-5M15 6l-4-5" stroke="var(--green)" stroke-width="2" fill="none"/>
    </svg>
    <span class="cart-label">My cart :</span>
    <span class="cart-count">Item (0)</span>
  </div>

  <nav class="abs main-nav">
    <a href="#">Home</a><a href="#">About us</a><a href="#">Products</a><a href="#">Partners</a><a href="#">Contact us</a>
  </nav>

  <div class="abs hero-ornament" role="img" aria-label="Pale green floral swirl decoration"></div>
  <div class="abs hero-shirt" role="img" aria-label="Green t-shirt printed with an enchanted forest and moonlit lake"></div>
  <h1 class="abs script hero-title">T- Shirt</h1>
  <p class="abs hero-text">Sed ut perspiciatis unde omnis iste natus error sit voluptatem accusantium doloremque laudantium, totam rem aperiam, eaque ipsa quae ab illo inven-tore veritatis et</p>
  <div class="abs btn-quote">GET A QUOTE</div>
  <svg class="abs slider-dots" width="80" height="16" viewBox="0 0 80 16" aria-hidden="true">
    <circle cx="8" cy="8" r="7" fill="#e6e6e6" stroke="#cccccc"/>
    <circle cx="29" cy="8" r="7" fill="var(--green)"/>
    <circle cx="50" cy="8" r="7" fill="var(--green)"/>
    <circle cx="71" cy="8" r="7" fill="var(--green)"/>
  </svg>

  <div class="abs divider"></div>

  <h2 class="abs script section-title featured-title">Featured Products</h2>
  <svg class="abs carousel-arrow" style="left:16px" width="28" height="42" viewBox="0 0 28 42" aria-hidden="true">
    <path d="M22 3L6 21l16 18" fill="none" stroke="#b5b5b5" stroke-width="6"/>
  </svg>
  <div class="abs product-card" style="left:65px"><div class="product-art art-black" role="img" aria-label="Black t-shirt with green tree print"></div></div>
  <div class="abs product-card" style="left:289px"><div class="product-art art-black" role="img" aria-label="Black t-shirt with green tree print"></div></div>
  <div class="abs product-card" style="left:512px"><div class="product-art art-green" role="img" aria-label="Green t-shirt with forest scene print"></div></div>
  <div class="abs product-card" style="left:736px"><div class="product-art art-green" role="img" aria-label="Green t-shirt with forest scene print"></div></div>
  <svg class="abs carousel-arrow" style="left:956px" width="28" height="42" viewBox="0 0 28 42" aria-hidden="true">
    <path d="M6 3l16 18L6 39" fill="none" stroke="#b5b5b5" stroke-width="6"/>
  </svg>

  <h2 class="abs script section-title welcome-title">Welcome to Our Website</h2>
  <p class="abs welcome-text">Lorem ipsum dolor sit amet, consectetur adipisicing elit, sed do eiusmod tempor incididunt ut labore et dolore magna aliqua. Ut enim ad minim veniam, quis nostrud exercitation ullamco laboris nisi ut aliquip ex ea commodo consequat. Duis aute irure dolor in reprehenderit in voluptate velit esse cillum</p>

  <div class="abs call-box"></div>
  <div class="abs call-photo" role="img" aria-label="Customer support agent wearing a headset"></div>
  <div class="abs call-title">CALL US</div>
  <div class="abs call-phone">+ 06 014 778 2093</div>
  <div class="abs btn-call">CLICK HERE</div>

  <div class="abs partners-band"></div>
  <h2 class="abs script partners-title">Our Partners</h2>
  <p class="abs partners-sub">We carry a wide selection of products.</p>
  <div class="abs partner-badge" style="left:425px;width:90px"></div>
  <div class="abs partner-badge" style="left:535px;width:120px"></div>
  <div class="abs partner-badge" style="left:678px;width:74px"></div>
  <div class="abs partner-badge" style="left:775px;width:97px"></div>
  <svg class="abs" style="left:893px;top:1065px" width="20" height="28" viewBox="0 0 20 28" aria-hidden="true">
    <path d="M4 3l11 11L4 25" fill="none" stroke="#b5b5b5" stroke-width="5"/>
  </svg>

  <footer class="abs footer"></footer>
  <nav class="abs footer-nav">
    <a href="#">Home</a><a href="#">About us</a><a href="#">Products</a><a href="#">Partners</a><a href="#">Contact us</a>
  </nav>
  <div class="abs follow">Follow us :</div>
  <div class="abs social" style="left:777px;background:var(--social-navy)"></div>
  <div class="abs social" style="left:820px;background:var(--social-sky)"></div>
  <div class="abs social" style="left:864px;background:var(--social-deep)"></div>
  <div class="abs social" style="left:907px;background:var(--social-orange)"></div>

  <div class="abs copyright">© 2012.www.mirovak.com</div>
</body>
</html>
```